I-71 Website for Washington D.C Cannabis Business

We need a website with a 21+ age (yes/no/captcha) verification
5 Pages listed on a top banner
Home/Splash Page-Should send back to splash & ask for 21+ veri
Shop-
about Us
Blog
Contact us:

Content for pages:
Splash Page - Contains How it works with 1-6 steps
1. Register for Rewards Or Head to {Link} for more anonymous Use
2. Choose Cookies & Free Gifts
3. Submit Address & Order
4.Recieve Confirmation Text
5.Send Separate Selfie and Clear Drivers License Picture
6.Enjoy Your Cookies and Free Gifts

Shop/Menu Page - Empty with top banner (will fill in this section)

Home- Should link back to Splash page
About Us-
"Welcome to Marlow Treats, where everyday is a marlow day! We believe that everyone who chooses to enjoy the medicinal and relaxing benefits cannabis, should have safe and reliable access. And no matter your lifestyle or level of wellness, you deserve access to friendly customer service and professional courtesy. At Marlow Treats we provide Artisan Cookies that come with I-71 Gifted premium exotic cannabis + edibles & accessories. We provide an excellent variety of cookies and gifts, and all purchases improve your community!

For every 5 Cookies you purchase we donate 50 Sandwiches to Local DC Organizations that help our community members in need. In this way, you’ll be supporting the local DC community by purchasing from Marlow Treats (We also have Sandwich Rewards!!)

Marlow Treats is and always will be committed to providing DC The Best Service, Gifts & Experience. Always. We are committed to setting a standard for the gifting business in DC.

We appreciate you taking the time to check us out! We are here for all of your I-71 compliant needs.

Need to reach us? Please send all business related inquiries/compliments/complaints to marlowtreatsdc@brimvale.com and we will reach out ASAP. We look forward to hearing from you!

-MT

Blog- This should be Fillable
Contact US: Should be fillable with text or graphic

Similar Websites to check out: https://www.dcfernlotte.com/
https://www.amberloftwick.com/

Target Market(s)

DC/Cannabis market

Coding

Coded - Design and coding required

Number of Pages Required

5+ page

Font styles to use
Other font styles liked:
• Sans Serif

Colors
0455a3
33b8a4
ffffff

Requirements
Must have
• 21+ age (yes/no/captcha) verification
I-71 Compliant
Color match the green to the logo
Nice to have
• I would like the website to have a fresh and fun look....without being corny
Cookie buttons (menu etc that look like a cookie)
Should not have
• No pictures of Marihuana

```html
<!DOCTYPE html>
<html lang="en">
<head>
<meta charset="utf-8">
<title>Marlow Treats – Home</title>
<link href="https://fonts.googleapis.com/css2?family=Montserrat:wght@500;600;700;800&family=Roboto:wght@400&family=Yellowtail&display=swap" rel="stylesheet">
<style>
:root{
  --brand-blue:#0455a3;
  --brand-teal:#33b8a4;
  --brand-green:#1fe02a;
  --white:#ffffff;
  --page-bg:#ebebeb;
  --text-dark:#333333;
  --button-grey:#c4c4c4;
  --button-blue:#2626dc;
}
*{margin:0;padding:0;box-sizing:border-box}
html,body{width:1200px;height:938px;overflow:hidden}
body{background:var(--page-bg);font-family:"Montserrat",sans-serif;position:relative}

.screen{position:absolute;top:72px;width:560px;height:794px;background:var(--white);overflow:hidden;box-shadow:0 1px 4px rgba(0,0,0,.12)}
.screen--gate{left:31px}
.screen--home{left:611px}

/* header */
.site-header{position:absolute;left:0;top:0;width:560px;height:58px;background:var(--white);z-index:3}
.brand-tab{position:absolute;left:51px;top:0;width:110px;height:71px;background:var(--white);clip-path:polygon(0 0,100% 0,100% 82%,93% 100%,7% 100%,0 82%);z-index:4}
.brand{position:absolute;left:0;right:0;top:22px;display:flex;flex-direction:column;align-items:center;gap:5px}
.brand-dot{width:16px;height:16px;border-radius:50%;background:var(--brand-green)}
.brand-name{font-weight:700;font-size:7.6px;color:#1f2fd0;letter-spacing:.3px;white-space:nowrap}
.main-nav{position:absolute;top:24px;left:0;font-size:6.4px;font-weight:500;color:#222}
.main-nav a{position:absolute;top:0;white-space:nowrap;text-decoration:none;color:#222}
.main-nav a.is-active{color:var(--brand-blue)}
.cart{position:absolute;left:481px;top:15px;width:27px;height:27px;border-radius:50%;background:var(--brand-blue);color:var(--white);display:flex;flex-direction:column;align-items:center;justify-content:center;font-family:"Roboto",sans-serif;font-size:5.5px;line-height:1}
.cart svg{margin-top:1px}

/* hero */
.hero{position:absolute;left:0;top:58px;width:560px;height:332px;
  background:
    radial-gradient(ellipse 40% 30% at 35% 30%,rgba(225,160,40,.55),transparent 70%),
    radial-gradient(ellipse 45% 35% at 50% 55%,#9a6a3e,transparent 75%),
    radial-gradient(ellipse 60% 50% at 50% 70%,#5b3a20,transparent 80%),
    linear-gradient(160deg,#4a3524 0%,#2e2016 45%,#3b2616 100%);}
.hero-title{position:absolute;left:0;right:0;top:98px;text-align:center;font-weight:800;font-size:30px;letter-spacing:.5px;color:var(--white)}
.hero-tagline{position:absolute;left:0;right:0;top:137px;text-align:center;font-family:"Yellowtail","Brush Script MT","Segoe Script",cursive;font-size:28px;color:var(--brand-green)}
.hero-button{position:absolute;left:237px;top:190px;width:86px;height:28px;border:2px solid var(--brand-green);border-radius:15px;background:var(--white);color:#1d2a3a;font-weight:700;font-size:8.6px;display:flex;align-items:center;justify-content:center;letter-spacing:.3px}

/* how it works */
.how-it-works{position:absolute;left:0;top:390px;width:560px;height:361px;background:var(--white)}
.section-title{position:absolute;left:0;right:0;top:28px;text-align:center;font-weight:700;font-size:15.5px;color:var(--brand-blue);letter-spacing:.3px}
.section-subtitle{position:absolute;left:0;right:0;top:49px;text-align:center;font-family:"Yellowtail","Brush Script MT","Segoe Script",cursive;font-size:12px;color:var(--brand-teal)}
.steps{position:absolute;left:0;top:0}
.step-label{position:absolute;transform:translateX(-50%);text-align:center;font-weight:500;font-size:7.2px;line-height:11.6px;color:var(--text-dark);white-space:nowrap}

/* footer */
.site-footer{position:absolute;left:0;bottom:0;width:560px;height:43px;background:var(--brand-blue);color:var(--white);font-family:"Roboto",sans-serif;font-size:7.4px;display:flex;align-items:center;justify-content:center}

/* age gate */
.age-overlay{position:absolute;inset:0;background:rgba(0,0,0,.64);z-index:10}
.age-modal{position:absolute;left:122px;top:152px;width:316px;height:194px;background:var(--white);z-index:11;text-align:center}
.age-modal .brand{top:22px}
.age-modal .brand-dot{width:22px;height:22px}
.age-modal .brand-name{font-size:8.6px}
.age-copy{position:absolute;left:20px;right:20px;top:84px;font-family:Arial,Helvetica,sans-serif;font-size:8px;line-height:14px;color:#333}
.age-question{position:absolute;left:0;right:0;top:121px;font-weight:600;font-size:12.2px;color:#333}
.age-button{position:absolute;top:150px;width:86px;height:23px;border:none;color:var(--white);font-family:"Montserrat",sans-serif;font-weight:500;font-size:11.5px;display:flex;align-items:center;justify-content:center}
.age-button--no{left:69px;background:var(--button-grey)}
.age-button--yes{left:162px;background:var(--button-blue)}
</style>
</head>
<body>

<!-- ===== Age verification screen ===== -->
<section class="screen screen--gate">
  <header class="site-header">
    <nav class="main-nav">
      <a class="is-active" style="left:253px">HOME</a>
      <a style="left:295px">SHOP</a>
      <a style="left:337px">ABOUT US</a>
      <a style="left:393px">BLOG</a>
      <a style="left:434px">CONTACT US</a>
    </nav>
    <div class="cart"><span>0</span>
      <svg width="8" height="7" viewBox="0 0 8 7"><path d="M0 .5h1.4l1 4h4l1-3H2" fill="none" stroke="#fff" stroke-width=".8"/><circle cx="2.8" cy="6.1" r=".6" fill="#fff"/><circle cx="5.8" cy="6.1" r=".6" fill="#fff"/></svg>
    </div>
  </header>
  <div class="brand-tab"><div class="brand"><span class="brand-dot"></span><span class="brand-name">MARLOW TREATS</span></div></div>
  <div class="hero" role="img" aria-label="Photo of chocolate chip cookies in a woven basket with star anise and orange slices"></div>

  <section class="how-it-works">
    <h2 class="section-title">HOW IT WORKS</h2>
    <p class="section-subtitle">Sed ut perspiciatis unde omnis iste natus error sit</p>
    <svg class="steps" width="560" height="361" viewBox="0 0 560 361">
      <use href="#steps-path"/>
    </svg>
    <div class="step-label" style="left:169px;top:102px">CHOOSE COOKIES<br>&amp; FREE GIFTS</div>
    <div class="step-label" style="left:313px;top:102px">RECIEVE<br>CONFIRMATION TEXT</div>
    <div class="step-label" style="left:469px;top:102px">ENJOY YOUR COOKIES<br>&amp; FREE GIFTS</div>
    <div class="step-label" style="left:92px;top:267px">REGISTER FOR<br>REWARDS</div>
    <div class="step-label" style="left:247px;top:268px">SUBMIT ADDRESS<br>&amp; ORDER</div>
    <div class="step-label" style="left:399px;top:268px">SEND SEPARATE<br>SELFIE AND&amp; CLEAR DRIVERS<br>LICENSE PICTURE</div>
  </section>

  <footer class="site-footer">© Copyrights 2021 Marlow Treats.All Rights Reserved.</footer>

  <div class="age-overlay"></div>
  <div class="age-modal" role="dialog" aria-label="Age verification">
    <div class="brand"><span class="brand-dot"></span><span class="brand-name">MARLOW TREATS</span></div>
    <p class="age-copy">At vero eos et accusamus et iusto odio dignissimos ducimus qui blanditiis praesentium voluptatum deleniti atque corrupti</p>
    <p class="age-question">YOU MUST BE 21 OR OLDER TO ENTER</p>
    <button class="age-button age-button--no">NO</button>
    <button class="age-button age-button--yes">YES</button>
  </div>
</section>

<!-- ===== Home screen ===== -->
<section class="screen screen--home">
  <header class="site-header">
    <nav class="main-nav">
      <a class="is-active" style="left:253px">HOME</a>
      <a style="left:295px">SHOP</a>
      <a style="left:337px">ABOUT US</a>
      <a style="left:393px">BLOG</a>
      <a style="left:434px">CONTACT US</a>
    </nav>
    <div class="cart"><span>0</span>
      <svg width="8" height="7" viewBox="0 0 8 7"><path d="M0 .5h1.4l1 4h4l1-3H2" fill="none" stroke="#fff" stroke-width=".8"/><circle cx="2.8" cy="6.1" r=".6" fill="#fff"/><circle cx="5.8" cy="6.1" r=".6" fill="#fff"/></svg>
    </div>
  </header>
  <div class="brand-tab"><div class="brand"><span class="brand-dot"></span><span class="brand-name">MARLOW TREATS</span></div></div>
  <div class="hero" role="img" aria-label="Photo of chocolate chip cookies in a woven basket with star anise and orange slices">
    <h1 class="hero-title">MARLOW TREATS</h1>
    <p class="hero-tagline">Where everyday is a marlow day</p>
    <a class="hero-button">SHOP NOW</a>
  </div>

  <section class="how-it-works">
    <h2 class="section-title">HOW IT WORKS</h2>
    <p class="section-subtitle">Sed ut perspiciatis unde omnis iste natus error sit</p>
    <svg class="steps" width="560" height="361" viewBox="0 0 560 361">
      <defs>
        <linearGradient id="step-stroke" gradientUnits="userSpaceOnUse" x1="0" y1="130" x2="0" y2="262">
          <stop offset="0" stop-color="#2fb8a6"/>
          <stop offset="1" stop-color="#0455a3"/>
        </linearGradient>
        <g id="steps-path" fill="none" stroke="url(#step-stroke)" stroke-width="1.6">
          <circle cx="54" cy="133.6" r="3" fill="#2fb8a6" stroke="none"/>
          <line x1="54" y1="134" x2="54.4" y2="223"/>
          <line x1="506.7" y1="171.5" x2="507" y2="263.8"/>
          <circle cx="507" cy="263.8" r="3" fill="#0455a3" stroke="none"/>
          <circle cx="92" cy="223" r="37.4"/>
          <circle cx="243" cy="223" r="37.4"/>
          <circle cx="393.5" cy="223" r="37.4"/>
          <circle cx="168" cy="171.5" r="37.4"/>
          <circle cx="318.8" cy="171.5" r="37.4"/>
          <circle cx="469.3" cy="171.5" r="37.4"/>
          <g stroke-width="1.3">
            <path d="M117 194.5l3.5 1.3-.3 3.6"/>
            <path d="M268 194.5l3.5 1.3-.3 3.6"/>
            <path d="M418.5 194.5l3.5 1.3-.3 3.6"/>
            <path d="M192 199l3.3-.8.2 3.5"/>
            <path d="M343 199l3.3-.8.2 3.5"/>
            <path d="M493.5 199l3.3-.8.2 3.5"/>
          </g>
          <g stroke="#3a3a3a" stroke-width=".9">
            <!-- register -->
            <rect x="76" y="224" width="32" height="7"/>
            <path d="M79 224v-9h26v9M84 215v-5h6v5M94 212h8v3"/>
            <path d="M86 227h12"/>
            <!-- cookies -->
            <circle cx="162" cy="170" r="11"/>
            <path d="M168 161a11 11 0 1 1-1 20"/>
            <circle cx="158" cy="166" r="1.3"/><circle cx="165" cy="173" r="1.3"/><circle cx="157" cy="175" r="1"/><circle cx="176" cy="173" r="1.1"/>
            <!-- document and clock -->
            <path d="M233 210h12v27h-15v-22z"/>
            <path d="M233 220h9M233 225h9M233 230h9"/>
            <circle cx="251" cy="210" r="6"/><path d="M251 207v3h2"/>
            <!-- envelopes -->
            <rect x="304" y="166" width="22" height="14"/><path d="M304 166l11 8 11-8"/>
            <rect x="312" y="160" width="22" height="14"/><path d="M312 160l11 8 11-8"/>
            <path d="M303 162h6M305 159h5"/>
            <!-- id card -->
            <rect x="375" y="213" width="36" height="22" rx="2"/>
            <circle cx="385" cy="220" r="3"/><path d="M380 230a5 5 0 0 1 10 0z"/>
            <path d="M394 219h12M394 224h12M394 229h9"/>
            <!-- gift -->
            <rect x="457" y="168" width="25" height="16"/><rect x="455" y="163" width="29" height="5"/>
            <path d="M469.5 163v21M469.5 163c-3-6-8-5-7-2s7 2 7 2c3-6 8-5 7-2s-7 2-7 2"/>
          </g>
        </g>
      </defs>
      <use href="#steps-path"/>
    </svg>
    <div class="step-label" style="left:169px;top:102px">CHOOSE COOKIES<br>&amp; FREE GIFTS</div>
    <div class="step-label" style="left:313px;top:102px">RECIEVE<br>CONFIRMATION TEXT</div>
    <div class="step-label" style="left:469px;top:102px">ENJOY YOUR COOKIES<br>&amp; FREE GIFTS</div>
    <div class="step-label" style="left:92px;top:267px">REGISTER FOR<br>REWARDS</div>
    <div class="step-label" style="left:247px;top:268px">SUBMIT ADDRESS<br>&amp; ORDER</div>
    <div class="step-label" style="left:399px;top:268px">SEND SEPARATE<br>SELFIE AND&amp; CLEAR DRIVERS<br>LICENSE PICTURE</div>
  </section>

  <footer class="site-footer">© Copyrights 2021 Marlow Treats.All Rights Reserved.</footer>
</section>

</body>
</html>
```